New Architectural Firm Business Cards

New Business card to compliment previous pixel harbor logo (attached). Please design a business card that is simple, modern, creative....please do not use "symbols", simply the logo and associated graphics/text. The front should contain name/address/phone/email/web address (with graphics).....back should be 100% graphic design using the logo somehow. Hoping for a two color (black and yellow) design. full bleed design, no borders

Target Market(s)

Commercial Architecture Clients

Industry/Entity Type

Architecture

Contact Information for Business Card

Please design a business card that is simple, modern, creative....please do not use "symbols", simply the logo and associated graphics/text. The front should contain name/address/phone/email/web address (with graphics).....back should be 100% graphic design using the logo somehow

Font styles to use
Sans Serif

Colors
FFF300
FFF600
FEFA6F
FFFEC7
FFFEE8

Requirements
Must have
• Clean, Modern Design
Should not have
• Stock images or "icons"

```html
<!DOCTYPE html>
<html lang="en">
<head>
<meta charset="utf-8">
<title>Pixel Harbor Architecture – Business Card</title>
<link rel="stylesheet" href="https://fonts.googleapis.com/css2?family=Roboto:wght@700&family=Tenor+Sans&display=swap">
<style>
  :root {
    --backdrop: #3a3a3a;
    --paper: #ffffff;
    --paper-shade: #f1f1f1;
    --yellow: #f0bd12;
    --yellow-deep: #d8a612;
    --yellow-pale: #f8ecc0;
    --ink: #231f20;
  }
  * { margin: 0; padding: 0; box-sizing: border-box; }
  html, body {
    width: 1200px;
    height: 900px;
    overflow: hidden;
    background: var(--backdrop);
    font-family: "Tenor Sans", "Helvetica Neue", sans-serif;
    color: var(--ink);
  }
  .canvas {
    position: relative;
    width: 1200px;
    height: 900px;
  }
  .card {
    position: absolute;
    left: 250px;
    width: 700px;
    height: 400px;
    background: linear-gradient(120deg, var(--paper) 40%, var(--paper-shade));
    overflow: hidden;
  }
  .card--back { top: 40px; }
  .card--front { top: 470px; }

  /* Back */
  .back-pattern {
    position: absolute;
    inset: 0;
    background: linear-gradient(135deg, var(--yellow-pale), #fbf5dd 55%, var(--paper));
  }
  .back-brand {
    position: absolute;
    left: 0; right: 0;
    top: 178px;
    text-align: center;
    font-size: 36px;
    color: var(--yellow);
  }

  /* Front */
  .front-art {
    position: absolute;
    inset: 0;
    width: 700px;
    height: 400px;
  }
  .brand {
    position: absolute;
    right: 48px;
    top: 46px;
    text-align: right;
  }
  .brand__name {
    font-size: 40px;
    line-height: 1;
    color: var(--yellow);
  }
  .brand__tag {
    margin-top: 8px;
    font-family: "Roboto", Arial, sans-serif;
    font-weight: 700;
    font-size: 17px;
    letter-spacing: 1px;
    color: var(--ink);
  }
  .holder-name {
    position: absolute;
    left: 70px;
    top: 120px;
    font-size: 24px;
    letter-spacing: 1.5px;
    text-transform: uppercase;
  }
  .contact-list {
    position: absolute;
    left: 90px;
    top: 215px;
    list-style: none;
    font-size: 18px;
    line-height: 27px;
  }
  .contact-list .label { display: inline-block; width: 22px; }
  .rule {
    position: absolute;
    left: 70px;
    height: 2px;
    background: var(--ink);
  }
  .rule--top { top: 205px; width: 330px; left: 150px; }
  .rule--bottom { top: 305px; width: 330px; }
  .address {
    position: absolute;
    left: 90px;
    top: 318px;
    font-size: 18px;
    line-height: 26px;
  }
</style>
</head>
<body>
<main class="canvas">

  <section class="card card--back" aria-label="Card back">
    <div class="back-pattern" role="img" aria-label="Repeating pattern of pale yellow brand marks"></div>
    <div class="back-brand">pixel harbor</div>
  </section>

  <section class="card card--front" aria-label="Card front">
    <svg class="front-art" viewBox="0 0 700 400" aria-hidden="true">
      <defs>
        <linearGradient id="yellowField" x1="0" y1="0" x2="1" y2="0">
          <stop offset="0" stop-color="var(--yellow-deep)"/>
          <stop offset="1" stop-color="var(--yellow)"/>
        </linearGradient>
      </defs>
      <path d="M0,0 H255 C275,120 340,200 440,215 C540,230 585,320 575,400 H0 Z" fill="url(#yellowField)"/>
      <path d="M255,0 C275,120 340,200 440,215 C540,230 585,320 575,400" fill="none" stroke="var(--ink)" stroke-width="5"/>
    </svg>

    <div class="brand">
      <div class="brand__name">pixel harbor</div>
      <div class="brand__tag">ARCHITECTURE</div>
    </div>

    <h1 class="holder-name">Mara Ellison</h1>
    <div class="rule rule--top"></div>
    <ul class="contact-list">
      <li><span class="label">T</span>. (00) 0000 0000</li>
      <li><span class="label">E</span>. mara@pixelharbor.com</li>
      <li><span class="label">W</span>. www.pixelharbor.com</li>
    </ul>
    <div class="rule rule--bottom"></div>
    <address class="address" style="font-style:normal">
      11 dummy city, dummy place<br>
      P.O Box 0000 Dummy Land
    </address>
  </section>

</main>
</body>
</html>
```